弊社で製造・販売しているお酢のラベルデザインをお願いします。

商品は純りんご酢にはちみつを合わせた物で、4倍程度に希釈して健康飲料として利用してもらう物です。(料理にも使えます)

以前よりこの商品は500ml入りとして販売していましたが、昨今の原料費高騰等を受け、
容量を300mlに変更する事にしました。
瓶も、角瓶だったものを丸瓶に変更します。
ご愛顧いただいていたお客様に、なるべく「これまでのがすごく小さく(少なく)なってしまった・・・」という印象をもたれないように、全く新しいイメージのラベルデザインにしたいと考えています。

価格は1300円程度です。
お酢としては高額の商品ですので、「高級感」のあるデザインを希望します。

さらに、購入者のほとんどが女性ですので、女性が手に取りたくなるような
「かわいらしさ」あるいは「オシャレ感」、「健康」をイメージさせるデザインを希望します。

もちろん、スーパーや百貨店の売り場に並んだ際、他社の商品に埋もれない
目を引くデザインであってほしいと思います。

ラベルサイズは縦90mm×横145mm
瓶に巻いた際に正面に見える部分は、おおよそ90mm×73mm になります。

商品名は「やまぶき畑のしずく」
商品名以外に正面に見える部分に入れてほしい文言は以下の3つです。

「4倍濃縮タイプ」「国内産りんご果汁使用」「あなたの元気を応援!」

写真ファイルを添付しますが、
新しい瓶は丸型で色は緑。キャップはゴールドです。

これまでの商品写真も添付致します。
イメージの全く違うものを希望します。

今回は、既存の商品の容量を小さくするにあたり、これまでとは違う雰囲気である事を最大のポイントとしました。

当選ラベルは、これまでの「かわいらしい」イメージから、大人っぽさ、清楚で上品な雰囲気を感じさせ好感を得ました。
またりんご型の白地に商品名が映え、目を引きました。白地の面積は修正により、正面からりんご型がより見えるようにしました。
ピンクのバックは赤やゴールド系のデザインが多かった中で、一際優しさを感じさせ、
女性が手に取りたくなる商品だと思います。

以上の理由により選ばせていただきました。

この度は、弊社商品のラベルデザインに多くの提案をいただき、ありがとうございました。

「りんご」と「はちみつ」という、よくある組み合わせでしたが、
どのデザインもそれぞれによく練られており選定には大変時間を要しました。

今回はご縁がなかった皆様におかれましても、
またの機会がありましたら、是非もう一度お力をお貸しいただければと思います。
本来であればお一人お一人にお礼を申し上げるべきですのに、
このコメントをもってお礼に代えさせていただきます事、どうぞご容赦ください。

ご応募、本当にありがとうございました。

```html
<!DOCTYPE html>
<html lang="ja">
<head>
<meta charset="utf-8">
<title>やまぶき畑のしずく ラベル</title>
<link href="https://fonts.googleapis.com/css2?family=M+PLUS+Rounded+1c:wght@500;800&family=Shippori+Mincho:wght@500;700&display=swap" rel="stylesheet">
<style>
  :root {
    --backdrop: #f2f0ec;
    --label-white: #ffffff;
    --honey-orange: #f08a14;
    --honey-light: #f8b24a;
    --honey-deep: #e0700a;
    --apple-red: #c8202a;
    --apple-dark: #8e1018;
    --leaf-green: #5e9a3a;
    --text-white: #ffffff;
  }
  html, body {
    margin: 0;
    padding: 0;
    width: 1200px;
    height: 3184px;
    overflow: hidden;
    background: var(--backdrop);
  }
  .label {
    position: absolute;
    left: 130px;
    top: 940px;
    width: 940px;
    height: 1500px;
    background: var(--label-white);
    overflow: hidden;
    box-shadow: 0 6px 30px rgba(0,0,0,0.08);
  }
  .top-drip {
    position: absolute;
    left: 0;
    top: 0;
    width: 940px;
    height: 110px;
  }
  .tagline {
    position: absolute;
    top: 118px;
    left: 0;
    width: 100%;
    text-align: center;
    font-family: "Shippori Mincho", serif;
    font-weight: 700;
    font-size: 40px;
    color: var(--honey-orange);
    font-style: italic;
    letter-spacing: 2px;
  }
  .drop-icon {
    position: absolute;
    left: 452px;
    top: 182px;
    width: 36px;
    height: 52px;
  }
  .product-name {
    position: absolute;
    left: 110px;
    top: 250px;
    margin: 0;
    font-family: "M PLUS Rounded 1c", sans-serif;
    font-weight: 800;
    font-size: 118px;
    line-height: 126px;
    color: var(--honey-orange);
    letter-spacing: -2px;
  }
  .product-name span { display: block; }
  .concentrate-badge {
    position: absolute;
    left: 500px;
    top: 566px;
    padding: 4px 34px;
    border: 4px solid var(--honey-orange);
    border-radius: 40px;
    font-family: "M PLUS Rounded 1c", sans-serif;
    font-weight: 500;
    font-size: 38px;
    line-height: 48px;
    color: var(--honey-orange);
    background: var(--label-white);
    z-index: 2;
  }
  .apple-photo {
    position: absolute;
    left: 160px;
    top: 600px;
    width: 680px;
    height: 680px;
    background:
      radial-gradient(circle at 70% 18%, rgba(94,154,58,0.85) 0 9%, transparent 16%),
      radial-gradient(circle at 45% 55%, var(--apple-red) 0 38%, var(--apple-dark) 46%, rgba(255,255,255,0) 52%);
  }
  .wave-band {
    position: absolute;
    left: 0;
    top: 1130px;
    width: 940px;
    height: 370px;
  }
  .origin-note {
    position: absolute;
    left: 0;
    top: 1390px;
    width: 100%;
    text-align: center;
    font-family: "Shippori Mincho", serif;
    font-weight: 500;
    font-size: 38px;
    color: var(--text-white);
    letter-spacing: 3px;
  }
</style>
</head>
<body>
  <div class="label">
    <svg class="top-drip" viewBox="0 0 940 110" aria-hidden="true">
      <defs>
        <linearGradient id="honeyTop" x1="0" y1="0" x2="0" y2="1">
          <stop offset="0" stop-color="#f08a14"/>
          <stop offset="1" stop-color="#f8b24a"/>
        </linearGradient>
      </defs>
      <path d="M0 0 H940 V16 H520 C490 16 482 30 478 60 C475 86 465 98 470 98 C475 98 465 86 462 60 C458 30 450 16 420 16 H0 Z" fill="url(#honeyTop)"/>
    </svg>

    <div class="tagline">あなたの元気を応援!</div>

    <svg class="drop-icon" viewBox="0 0 36 52" aria-hidden="true">
      <path d="M18 2 C24 18 34 28 34 36 A16 16 0 0 1 2 36 C2 28 12 18 18 2 Z" fill="var(--honey-light)"/>
    </svg>

    <h1 class="product-name"><span>やまぶき畑の</span><span>しずく</span></h1>

    <div class="concentrate-badge">4倍濃縮タイプ</div>

    <div class="apple-photo" role="img" aria-label="水滴のついた赤いりんごと緑の葉の写真"></div>

    <svg class="wave-band" viewBox="0 0 940 370" preserveAspectRatio="none" aria-hidden="true">
      <defs>
        <linearGradient id="waveFill" x1="0" y1="0" x2="0" y2="1">
          <stop offset="0" stop-color="#f8b24a"/>
          <stop offset="0.5" stop-color="#f08a14"/>
          <stop offset="1" stop-color="#e0700a"/>
        </linearGradient>
      </defs>
      <path d="M0 150 C220 60 420 200 620 120 C760 64 860 70 940 90 V370 H0 Z" fill="#fcd9a0" opacity="0.7"/>
      <path d="M0 190 C240 110 430 250 640 170 C780 118 870 120 940 140 V370 H0 Z" fill="url(#waveFill)"/>
      <path d="M0 200 C240 130 430 262 640 184 C780 134 870 136 940 154" fill="none" stroke="#ffffff" stroke-width="4" opacity="0.8"/>
    </svg>

    <div class="origin-note">国内産りんご果汁使用</div>
  </div>
</body>
</html>
```